Re-style home page - eye-catching and unique design for social commerce website

We need a new concept design for Trondix's home page.
We don't want to make huge changes but creating a more professional and eye-catching style.

We need to look very serious like a professional services company and in the same time to look like a social network for e-commerce.

Our logo is very captive and you can use to creating something of harmonious.

This is a re-style and I'm excepted to see unique and fresh design like Glimmora.
Updates

Target Market(s)

e-commerce and social

Industry/Entity Type

Social

Number of Pages Required

1 page

Font styles to use
Serif
Sans Serif

Requirements
Must have
• An eye-catching result.
• Search bar with logo and Login How it works and business
• The slogan with login and signup.
• Footer links.
Nice to have
• I would like to open the home page and see only two clear ways:
• -Consumer
• --Search
• --The slogan
• --Login and Signup
• --How it works
• -Business
• --Go to Business area
• Background: City, Shopping.
Should not have
• Scrollbar style!

```html
<!DOCTYPE html>
<html lang="en">
<head>
<meta charset="utf-8">
<title>Trondix — Shop directly from your Profile</title>
<link rel="stylesheet" href="https://fonts.googleapis.com/css2?family=Roboto:wght@400;500;700&display=swap">
<style>
  :root {
    --sky-top: #2f5f92;
    --sky-mid: #3b5d86;
    --city-dark: #1d2f52;
    --city-warm: #8a4a4a;
    --road-glow: #d98a4a;
    --white: #ffffff;
    --tile-text: #c8336b;
    --tile-bg: #ffffff;
    --social-blue: #1f3fc8;
    --social-blue-dark: #1a34a6;
    --search-icon: #2b7de0;
    --divider: #e3e3e3;
  }
  * { margin: 0; padding: 0; box-sizing: border-box; }
  html, body { width: 1200px; height: 1155px; overflow: hidden; }
  body {
    position: relative;
    font-family: "Roboto", sans-serif;
    color: var(--white);
    background: var(--city-dark);
  }
  .city-backdrop {
    position: absolute; inset: 0;
    background:
      radial-gradient(ellipse 420px 300px at 1080px 980px, rgba(217,138,74,.55), transparent 70%),
      radial-gradient(ellipse 380px 260px at 120px 1000px, rgba(180,90,70,.45), transparent 70%),
      linear-gradient(180deg, var(--sky-top) 0%, var(--sky-mid) 35%, #2a3f66 60%, var(--city-warm) 85%, #5a3a4a 100%);
  }
  .site-header {
    position: absolute; left: 397px; top: 52px; width: 405px;
  }
  .search-bar {
    display: flex; height: 54px; background: var(--white);
  }
  .search-bar__field {
    flex: 1; display: flex; align-items: center; padding-left: 20px;
    font-size: 16px; color: #333;
  }
  .search-bar__button {
    width: 58px; border-left: 1px solid var(--divider);
    display: flex; align-items: center; justify-content: center;
  }
  .header-links {
    display: flex; justify-content: space-between; margin-top: 12px;
    font-size: 15px;
  }
  .brand {
    position: absolute; z-index: 2; left: 448px; top: 170px; width: 310px;
    display: flex; align-items: center; gap: 12px;
    font-size: 62px; font-weight: 700; letter-spacing: -1px; line-height: 1;
    color: var(--white);
  }
  .brand__mark { width: 44px; height: 44px; background: #e8673a; }
  .hero {
    position: absolute; z-index: 1; left: 191px; top: 210px; width: 819px; height: 818px;
  }
  .hero__photo {
    position: absolute; inset: 0;
    background:
      linear-gradient(100deg, rgba(200,200,200,.9) 0%, rgba(210,160,170,.8) 35%, rgba(170,140,110,.85) 60%, rgba(190,30,80,.9) 85%, rgba(90,20,40,.95) 100%);
  }
  .hero__content { position: absolute; inset: 0; text-align: center; }
  .hero__title {
    position: absolute; top: 54px; width: 100%;
    font-size: 39px; font-weight: 400;
  }
  .hero__subtitle {
    position: absolute; top: 136px; width: 100%;
    font-size: 29px; font-weight: 400;
  }
  .feed-tile {
    position: absolute; width: 194px; height: 53px;
    background: var(--tile-bg); color: var(--tile-text);
    display: flex; align-items: center; justify-content: center;
    text-align: center; font-size: 14.5px; line-height: 1.3; text-transform: uppercase;
  }
  .feed-tile--featured { font-size: 15.5px; font-weight: 500; }
  .hero__slogan {
    position: absolute; top: 660px; width: 100%; font-size: 24px;
  }
  .social-login {
    position: absolute; left: 304px; top: 704px; width: 223px; height: 44px;
    background: var(--social-blue); display: flex; align-items: center;
    font-size: 15px; font-weight: 700;
  }
  .social-login__icon {
    width: 49px; height: 100%; background: var(--social-blue-dark);
    display: flex; align-items: center; justify-content: center; margin-right: 12px;
  }
  .social-login__icon span { width: 14px; height: 14px; background: var(--white); }
  .hero__signup {
    position: absolute; top: 762px; width: 100%; font-size: 20px;
  }
  .site-footer {
    position: absolute; top: 1082px; width: 100%;
    text-align: center; font-size: 14px;
  }
  .site-footer span { margin: 0 6px; }
</style>
</head>
<body>
  <div class="city-backdrop" role="img" aria-label="Blurred city skyline at dusk with light trails on a highway"></div>

  <header class="site-header">
    <div class="search-bar">
      <div class="search-bar__field">Search here...</div>
      <div class="search-bar__button">
        <svg width="28" height="28" viewBox="0 0 28 28" aria-hidden="true">
          <circle cx="11" cy="11" r="8" fill="none" stroke="var(--search-icon)" stroke-width="3"/>
          <line x1="17" y1="17" x2="25" y2="25" stroke="var(--search-icon)" stroke-width="3.5" stroke-linecap="round"/>
        </svg>
      </div>
    </div>
    <nav class="header-links">
      <span>How it work / Business</span>
      <span>Login / Sign up</span>
    </nav>
  </header>

  <main class="hero">
    <div class="hero__photo" role="img" aria-label="Woman's arm holding a payment card and colourful shopping bags"></div>
    <div class="hero__content">
      <h1 class="hero__title">Shop directly from your Profile</h1>
      <h2 class="hero__subtitle">SETUP YOUR FEED</h2>

      <div class="feed-tile" style="left:110px;top:196px">Active Life</div>
      <div class="feed-tile" style="left:311px;top:196px">Arts &amp; Entertainment</div>
      <div class="feed-tile" style="left:514px;top:196px">Automotive</div>

      <div class="feed-tile" style="left:110px;top:258px">Beauti &amp; Spas</div>
      <div class="feed-tile feed-tile--featured" style="left:311px;top:258px">Education</div>
      <div class="feed-tile" style="left:514px;top:258px">Event Planning<br>&amp; Services</div>

      <div class="feed-tile feed-tile--featured" style="left:110px;top:320px">Financial Services</div>
      <div class="feed-tile" style="left:311px;top:320px">Food</div>
      <div class="feed-tile" style="left:514px;top:320px">Health &amp; Medical</div>

      <div class="feed-tile" style="left:110px;top:382px">Home Servies</div>
      <div class="feed-tile" style="left:311px;top:382px">Hotels</div>
      <div class="feed-tile" style="left:514px;top:382px">Local Services</div>

      <div class="feed-tile" style="left:110px;top:444px">Mass Media</div>
      <div class="feed-tile" style="left:311px;top:444px">Nightlife</div>
      <div class="feed-tile" style="left:514px;top:444px">Pets</div>

      <div class="feed-tile" style="left:110px;top:506px">Professional<br>Services</div>
      <div class="feed-tile" style="left:311px;top:506px">Public Services &amp;<br>Goverment</div>
      <div class="feed-tile" style="left:514px;top:506px">Real Estate</div>

      <div class="feed-tile feed-tile--featured" style="left:209px;top:568px">Restaurants</div>
      <div class="feed-tile feed-tile--featured" style="left:411px;top:568px">Shopping</div>

      <p class="hero__slogan">Save Your Time. Live Better</p>
      <div class="social-login">
        <div class="social-login__icon"><span></span></div>
        Login with Friendora
      </div>
      <p class="hero__signup">Sign Up</p>
    </div>
  </main>

  <div class="brand"><span>Trondix</span><span class="brand__mark"></span></div>

  <footer class="site-footer">
    About us<span>|</span>Blog<span>|</span>Business Jobs<span>|</span>Privacy<span>|</span>FAQ<span>|</span>Contacts
  </footer>
</body>
</html>
```